A Lantern on the pier.

I need a book cover (and back cover) design for a novel. The novel is a thiller. ´Synopsis: During the party after an awards ceremony at prestigious institution, one of the young awarders dissapear. The last place where he left a trace was close to a giant chessboard in the grass of the beautiful gardens of the place of ceremony. The detective in charge of finding the missing person and find out what happened will gradually discover that the institution is not all that it seems.
The book cover size will be 9" x 6" and the title of the novel "A lantern on the pier" will be name in spanish "Una linterna en el muelle". The back cover will have a synopsis (in spanish )that i will develop later on.
One suggestion for the design: I always love the art of MILO TRENT for movie posters, so I´m looking for something of similar style, you know (the girl who sold paper kites, North pier ballad, halvorn, ledger of shadows, etc

```html
<!DOCTYPE html>
<html lang="es">
<head>
<meta charset="utf-8">
<title>Una linterna en el muelle — cubierta</title>
<link rel="stylesheet" href="https://fonts.googleapis.com/css2?family=EB+Garamond&family=Open+Sans:wght@700&family=Oswald:wght@500&display=swap">
<style>
  :root {
    --page: #f1f1f1;
    --cover-red: #e21b2b;
    --ink: #0c0c0c;
    --board-dark: #151515;
    --board-mid: #4a0e14;
    --paper: #ffffff;
  }
  * { margin: 0; padding: 0; box-sizing: border-box; }
  html, body { width: 899px; height: 1200px; overflow: hidden; background: var(--page); }
  .spread {
    position: absolute; left: 10px; top: 296px;
    width: 880px; height: 608px;
    background: var(--cover-red);
    overflow: hidden;
    box-shadow: 0 2px 8px rgba(0,0,0,.15);
  }
  .back-blurb {
    position: absolute; left: 36px; top: 45px; width: 346px;
    font-family: "EB Garamond", serif; font-size: 12.4px; line-height: 15.7px;
    color: var(--paper); text-align: justify;
  }
  .pawn-silhouette {
    position: absolute; left: 0; top: 246px; width: 160px; height: 362px;
    background: var(--ink);
    border-radius: 0 90px 0 0;
  }
  .barcode-box {
    position: absolute; left: 269px; top: 510px; width: 101px; height: 66px;
    background: var(--paper);
  }
  .spine {
    position: absolute; left: 425px; top: 0; width: 50px; height: 608px;
  }
  .spine-title, .spine-author {
    position: absolute; left: 50%; white-space: nowrap;
    font-family: "Open Sans", sans-serif; font-weight: 700; color: var(--paper);
    transform: translate(-50%, -50%) rotate(-90deg);
  }
  .spine-title { top: 145px; font-size: 16px; }
  .spine-author { top: 470px; font-size: 10.5px; letter-spacing: 4px; }
  .spine-mark {
    position: absolute; left: 19px; top: 300px; width: 12px; height: 12px;
    background: var(--ink); border-radius: 50%;
  }
  .front { position: absolute; left: 475px; top: 0; width: 405px; height: 608px; }
  .front-tagline {
    position: absolute; top: 30px; width: 100%; text-align: center;
    font-family: "Open Sans", sans-serif; font-weight: 700; font-size: 9px;
    color: var(--paper);
  }
  .board-art { position: absolute; left: 23px; top: 193px; width: 343px; height: 182px; }
  .front-title {
    position: absolute; left: 0; top: 386px; width: 100%; text-align: center;
    font-family: "Oswald", sans-serif; font-weight: 500; font-size: 40px;
    line-height: 44px; text-transform: uppercase; color: var(--paper);
  }
  .front-author {
    position: absolute; left: 0; top: 550px; width: 100%; text-align: center;
    font-family: "Open Sans", sans-serif; font-weight: 700; font-size: 21px;
    letter-spacing: 9px; color: var(--paper);
  }
</style>
</head>
<body>
  <main class="spread">
    <section class="back-cover">
      <p class="back-blurb">Lorem ipsum dolor sit amet, consectetur adipiscing elit. Sed interdum ullamcorper ligula, sit amet gravida nulla lobortis mollis. Pellentesque semper orci lacus, tincidunt varius tortor faucibus sed. In aliquam finibus mi sed placerat. Pellentesque a aliquam ligula. Vestibulum massa nibh, facilisis sed nisl a, congue maximus massa. Aenean non nulla sit amet ex cursus scelerisque. Suspendisse potenti. In luctus pellentesque justo. Vivamus blandit, libero vitae suscipit bibendum, ipsum felis porta ex, vel commodo odio lacus vel mauris. Vestibulum luctus vel dui quis volutpat. Curabitur ligula magna, varius euismod libero at, consequat fringilla mauris. Quisque iaculis sit amet justo vitae venenatis.</p>
      <div class="pawn-silhouette" role="img" aria-label="Silueta negra de un peón de ajedrez"></div>
      <div class="barcode-box"></div>
    </section>
    <section class="spine">
      <span class="spine-title">UNA LINTERNA EN EL MUELLE</span>
      <span class="spine-mark"></span>
      <span class="spine-author">TOMAS VELARDE</span>
    </section>
    <section class="front">
      <p class="front-tagline">LOREM IPSUM DOLOR SIT AMET, CONSECTETUR ADIPISCING ELIT.</p>
      <svg class="board-art" viewBox="0 0 343 182" role="img" aria-label="Tablero de ajedrez gigante en perspectiva sobre el césped, con huellas de pasos sobre una casilla">
        <defs>
          <linearGradient id="boardTone" x1="0" y1="0" x2="0" y2="1">
            <stop offset="0" stop-color="var(--board-mid)"/>
            <stop offset="1" stop-color="var(--board-dark)"/>
          </linearGradient>
        </defs>
        <polygon points="107,0 255,0 343,30 187,182 0,46" fill="url(#boardTone)"/>
      </svg>
      <h1 class="front-title">Una linterna<br>en el muelle</h1>
      <p class="front-author">TOMAS VELARDE</p>
    </section>
  </main>
</body>
</html>
```